Business Card Design Project

Need professional business card and Employee Badge design for a young dynamic and emp friendly IT Services company.

Target Market(s)

IT, Corporate

Industry/Entity Type

Business

Requirements
Must have
• Modern, Sleek, Prfessional, IT services
Should not have
• Too much diffrent colors

```html
<!DOCTYPE html>
<html lang="en">
<head>
<meta charset="utf-8">
<title>Corvana Systems – Business Card</title>
<link rel="stylesheet" href="https://fonts.googleapis.com/css2?family=Open+Sans:wght@400;600;700&display=swap">
<style>
  :root {
    --canvas: #e9e7e3;
    --card-white: #ffffff;
    --card-dark: #1c1c1d;
    --card-dark-2: #2e2e30;
    --brand-red: #d1293f;
    --accent-rust: #a5421f;
    --accent-grey: #8c8c8c;
    --text-light: #e8e8e8;
    --text-muted: #b5b5b5;
  }
  * { box-sizing: border-box; margin: 0; padding: 0; }
  html, body { width: 1200px; height: 1024px; overflow: hidden; }
  body {
    background: var(--canvas);
    font-family: "Open Sans", Arial, sans-serif;
    display: flex; flex-direction: column; align-items: center; justify-content: center;
    gap: 48px;
  }
  .card {
    position: relative; width: 700px; height: 400px; overflow: hidden;
    box-shadow: 0 10px 28px rgba(0,0,0,.18);
  }
  /* Front */
  .card--front { background: var(--card-dark); }
  .front-shapes { position: absolute; inset: 0; }
  .brand {
    position: absolute; left: 60px; top: 70px;
    font-weight: 700; font-size: 44px; color: var(--brand-red);
    letter-spacing: 1px; text-transform: lowercase;
  }
  .identity { position: absolute; left: 60px; top: 250px; color: var(--text-light); }
  .identity .name { font-weight: 700; font-size: 17px; text-transform: uppercase; letter-spacing: .5px; }
  .identity .title { font-weight: 700; font-size: 13px; text-transform: uppercase; margin-bottom: 12px; }
  .identity p { font-size: 13px; line-height: 1.45; color: var(--text-muted); }
  .contacts { position: absolute; left: 420px; top: 250px; list-style: none; }
  .contacts li {
    display: flex; align-items: center; gap: 10px;
    font-size: 13px; line-height: 1.75; color: var(--text-light);
  }
  .contacts svg { width: 12px; height: 12px; fill: var(--brand-red); flex: none; }
  /* Back */
  .card--back { background: var(--card-dark); }
  .back-texture {
    position: absolute; inset: 0;
    background: linear-gradient(160deg, #3a3a3c 0%, #1e1e20 45%, #2c2c2e 70%, #121213 100%);
  }
  .back-content {
    position: absolute; inset: 0;
    display: flex; flex-direction: column; align-items: center; justify-content: center; gap: 22px;
  }
  .back-content .brand { position: static; font-size: 60px; }
  .back-content .web { font-size: 15px; color: var(--text-light); letter-spacing: .5px; }
</style>
</head>
<body>
  <section class="card card--front" aria-label="Business card front">
    <svg class="front-shapes" viewBox="0 0 700 400" preserveAspectRatio="none" aria-hidden="true">
      <rect width="700" height="400" fill="var(--card-dark)"/>
      <polygon points="0,0 560,0 600,200 0,200" fill="var(--card-white)"/>
      <polygon points="560,0 600,0 610,150 600,200" fill="var(--accent-rust)"/>
      <polygon points="600,0 625,0 640,200 600,200" fill="var(--card-white)"/>
      <polygon points="625,0 700,0 700,200 640,200" fill="var(--accent-grey)"/>
      <rect y="200" width="700" height="8" fill="var(--card-dark-2)"/>
    </svg>
    <div class="brand">Corvana Systems</div>
    <div class="identity">
      <div class="name">Daniel Morrow</div>
      <div class="title">Job Title</div>
      <p>your address goes here,<br>state, city, zip code, country name<br>www.corvanasystems.com</p>
    </div>
    <ul class="contacts">
      <li><svg viewBox="0 0 24 24"><path d="M6.6 10.8a15 15 0 0 0 6.6 6.6l2.2-2.2a1 1 0 0 1 1-.25 11.4 11.4 0 0 0 3.6.57 1 1 0 0 1 1 1V20a1 1 0 0 1-1 1A17 17 0 0 1 3 4a1 1 0 0 1 1-1h3.5a1 1 0 0 1 1 1c0 1.25.2 2.45.57 3.57a1 1 0 0 1-.25 1z"/></svg>+1 555 0142 301</li>
      <li><svg viewBox="0 0 24 24"><rect x="3" y="5" width="18" height="14" rx="2"/></svg>+1 555 0142 302</li>
      <li><svg viewBox="0 0 24 24"><rect x="7" y="2" width="10" height="20" rx="2"/></svg>+1 555 0178 622</li>
      <li><svg viewBox="0 0 24 24"><path d="M3 5h18v14H3z M3 5l9 7 9-7" /></svg>dan@corvanasystems.com</li>
    </ul>
  </section>

  <section class="card card--back" aria-label="Business card back">
    <div class="back-texture" role="img" aria-label="Dark grey embossed pyramid stud texture"></div>
    <div class="back-content">
      <div class="brand">Corvana Systems</div>
      <div class="web">www.corvanasystems.com</div>
    </div>
  </section>
</body>
</html>
```